Pet sitting Business needs a website

We need a website that shows our services and prices. Shows our love of animals but also our professionalism. want a gallery, about, blog, services, links to fb and instagram accounts, newsletter archive. want it to be easy to access and wonderful to navigate. want the domain to be Brindlecovepawhouse.com
take any info from FB site www.facebook.com/brindlecovepawhouse
I would like it to fit square space platform

Target Market(s)

upscale area, responsible pet owners,

Industry/Entity Type

Pet Care

Coding

Coded - Design and coding required

Number of Pages Required

5+ page

Font styles to use
Sans Serif

Requirements
Must have
• (square space platform)
• Menu
• photo gallery
• about us
• services
• policies
• monthly newsletter
• unavailable dates
• Introduction (welcome)
• payment methods
• Daily updates
• testimonials (use from fb site)
Should not have
• stock photos

```html
<!DOCTYPE html>
<html lang="en">
<head>
<meta charset="utf-8">
<title>Brindle Cove Paw House</title>
<link href="https://fonts.googleapis.com/css2?family=Open+Sans:ital,wght@0,400;0,600;0,700;1,400;1,600&family=Roboto:ital,wght@0,400;0,500;0,700;1,700&display=swap" rel="stylesheet">
<style>
:root{
  --blue:#1a80bb;
  --blue-dark:#166ea3;
  --orange:#efa20c;
  --ink:#333;
  --muted:#666;
  --line:#d9d9d9;
  --white:#fff;
  --bar:#2a2a2a;
  --grass-a:#5f7d38;
  --grass-b:#2f4420;
  --forest-a:#2c3526;
  --forest-b:#151b13;
}
*{box-sizing:border-box;margin:0;padding:0}
html,body{width:1200px;height:3249px;overflow:hidden}
body{position:relative;font-family:"Open Sans",Arial,sans-serif;color:var(--ink);background:var(--white)}
.abs{position:absolute}
/* header */
.header{position:absolute;left:0;top:0;width:1200px;height:120px;background:var(--white);box-shadow:0 2px 6px rgba(0,0,0,.12);z-index:2}
.topbar{position:absolute;left:0;top:0;width:1200px;height:40px;background:var(--blue)}
.social{position:absolute;left:108px;top:9px;display:flex;gap:12px}
.social span{width:20px;height:20px;border-radius:50%;background:rgba(255,255,255,.9);display:block}
.contact-top{position:absolute;left:740px;top:10px;display:flex;gap:30px;color:#fff;font-size:15px}
.contact-top span{display:flex;align-items:center;gap:8px}
.nav{position:absolute;top:62px;display:flex;gap:14px;font-family:Roboto,sans-serif;font-size:13px;font-weight:500;color:#333;text-transform:uppercase;white-space:nowrap}
.nav a{color:inherit;text-decoration:none;padding:6px 10px}
.nav a.active{border:1px solid var(--blue);color:var(--blue);border-radius:3px}
.brand{position:absolute;left:509px;top:0;width:184px;height:170px;z-index:3}
.brand-name{position:absolute;left:0;top:58px;width:184px;text-align:center;font-family:Roboto,sans-serif;font-weight:500;font-size:20px;line-height:24px;color:var(--blue)}
.brand-dot{position:absolute;left:74px;top:14px;width:36px;height:36px;border-radius:50%;background:var(--orange)}
/* hero */
.hero{position:absolute;left:0;top:120px;width:1200px;height:530px;background:linear-gradient(180deg,#2e3d22 0%,var(--grass-b) 30%,var(--grass-a) 65%,#789848 100%)}
.hero-title{position:absolute;left:736px;top:352px;font-family:Roboto,sans-serif;font-weight:500;font-size:36px;color:#fff;letter-spacing:.5px}
.hero-text{position:absolute;left:736px;top:400px;width:370px;font-size:17px;line-height:22px;color:#fff}
.btn-blue{position:absolute;left:736px;top:462px;width:152px;height:42px;background:var(--blue);color:#fff;font-family:Roboto,sans-serif;font-size:15px;display:flex;align-items:center;justify-content:center}
.arrow{position:absolute;top:370px}
/* services */
.service{position:absolute;top:580px;width:260px;text-align:center}
.service .circle{width:220px;height:220px;margin:0 auto;border-radius:50%;border:7px solid var(--orange);background:linear-gradient(160deg,#6d8a4a,#3e5a2a)}
.service h3{margin-top:22px;font-family:Roboto,sans-serif;font-weight:500;font-size:18px;color:#222}
.service p{margin:8px auto 0;width:240px;font-size:12px;line-height:16px;color:var(--muted)}
.btn-outline{display:inline-block;margin-top:20px;border:1px solid var(--blue);color:var(--blue);font-size:10px;padding:5px 12px}
/* section heading */
.sec-title{position:absolute;left:0;width:1200px;text-align:center;font-family:Roboto,sans-serif;font-size:34px;font-weight:400;color:#222;letter-spacing:.3px}
.orn{position:absolute;left:480px;width:240px;height:30px}
.welcome-text{position:absolute;left:110px;top:1106px;width:980px;text-align:center;font-size:11.5px;line-height:21px;color:var(--muted)}
/* testimonials */
.testimonials{position:absolute;left:0;top:1220px;width:1200px;height:480px;background:linear-gradient(180deg,var(--forest-a),var(--forest-b))}
.quote{position:absolute;top:166px;width:314px;height:148px;background:rgba(255,255,255,.82);padding:22px 24px 0 24px;font-size:11.5px;line-height:18px;color:#444}
.quote::after{content:"";position:absolute;left:46px;bottom:-14px;border-left:14px solid transparent;border-right:14px solid transparent;border-top:14px solid rgba(255,255,255,.82)}
.quote b{font-family:Georgia,serif;color:#888;font-size:22px;margin-right:6px}
.author{position:absolute;top:332px;display:flex;align-items:center;gap:18px;color:#fff}
.avatar{width:78px;height:78px;border-radius:50%;border:3px solid #fff;background:linear-gradient(160deg,#c9a58a,#7b5a46)}
.author .name{font-family:"Open Sans",sans-serif;font-style:italic;font-size:15px}
.author .org{font-style:italic;font-size:12px;margin-top:3px}
/* gallery */
.gal{position:absolute;top:1852px;width:242px;height:318px}
.gal::after{content:"";position:absolute;inset:8px;border:1px solid rgba(255,255,255,.85)}
/* updates */
.updates{position:absolute;left:0;top:2242px;width:1200px;height:385px;background:linear-gradient(180deg,#2f3a28,#3b4a30 60%,#4f6238)}
.upd-icon{position:absolute;left:557px;top:52px;width:87px;height:87px;border-radius:50%;border:3px solid var(--orange);background:#1c2418}
.upd-icon span{position:absolute;left:24px;top:24px;width:33px;height:33px;border-radius:50%;background:var(--orange)}
.upd-title{position:absolute;left:0;top:158px;width:1200px;text-align:center;font-family:Roboto,sans-serif;font-weight:700;font-style:italic;font-size:31px;color:#fff}
.upd-sub{position:absolute;left:0;top:210px;width:1200px;text-align:center;font-size:16px;color:#fff}
.subscribe{position:absolute;left:325px;top:251px;width:550px;height:48px;display:flex}
.subscribe .field{flex:1;background:#fff;border-radius:24px 0 0 24px;font-size:14px;color:#888;display:flex;align-items:center;padding-left:28px}
.subscribe .go{width:138px;background:var(--orange);border-radius:0 24px 24px 0;color:#fff;font-family:Roboto,sans-serif;font-size:14px;font-weight:500;display:flex;align-items:center;justify-content:center}
/* news */
.news{position:absolute;left:0;top:2627px;width:1200px;height:313px;background:#f3f4f6}
.news-title{position:absolute;left:100px;top:38px;display:flex;align-items:center;gap:12px;font-family:Roboto,sans-serif;font-size:24px;color:#222}
.news-title span{width:26px;height:26px;border-radius:50%;background:var(--orange)}
.news-nav{position:absolute;left:1052px;top:46px;font-size:14px;color:#444;letter-spacing:14px}
.news-img{position:absolute;top:96px;width:186px;height:160px}
.news-body{position:absolute;top:96px;width:240px}
.news-body h4{font-family:Roboto,sans-serif;font-weight:400;font-size:16px;line-height:21px;color:#333}
.news-body .date{margin-top:10px;font-style:italic;font-size:13px;color:var(--blue)}
.news-body p{margin-top:10px;font-size:11px;line-height:17px;color:var(--muted)}
.news-body .more{margin-top:14px;font-size:13px;color:#444}
/* footer */
.footer{position:absolute;left:0;top:2940px;width:1200px;height:255px;background:var(--blue)}
.foot-brand{position:absolute;left:98px;top:80px;width:180px;text-align:center;font-family:Roboto,sans-serif;font-weight:500;font-size:22px;line-height:26px;color:#fff}
.foot-brand span{display:block;width:40px;height:40px;border-radius:50%;background:#fff;margin:0 auto 12px}
.foot-col{position:absolute;top:36px;color:#fff}
.foot-col h5{font-family:Roboto,sans-serif;font-weight:500;font-size:18px;margin-bottom:24px;letter-spacing:.3px}
.c-row{display:flex;gap:16px;font-size:12.5px;line-height:17px;margin-bottom:16px}
.links li{list-style:none;font-size:12.5px;line-height:25px}
.links li::before{content:"›";margin-right:8px}
.tweet{display:flex;gap:12px;margin-bottom:14px;font-size:11.5px;line-height:16px}
.tweet .tb{width:18px;height:18px;background:#fff;flex:none;margin-top:2px}
.tweet small{display:block;margin-top:6px;font-size:11px;opacity:.85}
.copy{position:absolute;left:0;top:3195px;width:1200px;height:54px;background:var(--bar);color:#ccc;font-size:12.5px;display:flex;align-items:center;justify-content:center}
</style>
</head>
<body>

<header class="header">
  <div class="topbar">
    <div class="social"><span></span><span></span><span></span><span></span></div>
    <div class="contact-top">
      <span><svg width="14" height="14" viewBox="0 0 24 24"><path fill="#fff" d="M6.6 10.8a15 15 0 0 0 6.6 6.6l2.2-2.2c.3-.3.7-.4 1-.2 1.1.4 2.3.6 3.6.6.6 0 1 .4 1 1V20c0 .6-.4 1-1 1A17 17 0 0 1 3 4c0-.6.4-1 1-1h3.5c.6 0 1 .4 1 1 0 1.3.2 2.5.6 3.6.1.3 0 .7-.2 1z"/></svg>+901.555.0142</span>
      <span><svg width="16" height="12" viewBox="0 0 16 12"><rect x="0.7" y="0.7" width="14.6" height="10.6" fill="none" stroke="#fff" stroke-width="1.4"/><path d="M1 1l7 6 7-6" fill="none" stroke="#fff" stroke-width="1.4"/></svg>info@brindlecovepawhouse.com</span>
    </div>
  </div>
  <nav class="nav" style="left:108px"><a class="active">Home</a><a>About Us</a><a>Services</a><a>Policies</a></nav>
  <nav class="nav" style="left:716px"><a>Gallery</a><a>Monthly Newsletter</a><a>Contact Us</a></nav>
</header>

<div class="brand">
  <svg class="abs" width="184" height="170" viewBox="0 0 184 170"><path d="M0 0H184V132L92 170L0 132Z" fill="#fff"/></svg>
  <span class="brand-dot"></span>
  <div class="brand-name">Brindle Cove<br>Paw House</div>
</div>

<section class="hero" role="img" aria-label="Photo of a boy playing with two black dogs on a backyard lawn"></section>
<svg class="arrow" style="left:34px" width="20" height="40" viewBox="0 0 20 40"><path d="M18 2L2 20l16 18" fill="none" stroke="rgba(255,255,255,.7)" stroke-width="2"/></svg>
<svg class="arrow" style="left:1146px" width="20" height="40" viewBox="0 0 20 40"><path d="M2 2l16 18L2 38" fill="none" stroke="rgba(255,255,255,.7)" stroke-width="2"/></svg>
<h1 class="hero-title">BRINDLE COVE PAW</h1>
<p class="hero-text">Hi my name is Marla Ostrand and I would love to introduce myself. I am a Licensed</p>
<div class="btn-blue">GET MORE INFO</div>

<div class="service" style="left:80px"><div class="circle" role="img" aria-label="Photo of a girl with a small dog on the grass"></div><h3>DAILY VISIT - $25.00</h3><p>No additional charge for each pet Dog walks or play time for your pet Feeding and fresh water Cleaning up any</p><span class="btn-outline">READ MORE</span></div>
<div class="service" style="left:336px"><div class="circle" role="img" aria-label="Photo of children gathered with a shaggy dog"></div><h3>POTTY VISITS - $10.00</h3><p>Usually done at noon and bedtime Medication letting them out to potty some playtime checking surroundings</p><span class="btn-outline">READ MORE</span></div>
<div class="service" style="left:600px"><div class="circle" role="img" aria-label="Photo of a dog on an agility course in a park"></div><h3>DOG PARK</h3><p>No additional charge for each pet Dog walks or play time for your pet Feeding and fresh water Cleaning up any</p><span class="btn-outline">READ MORE</span></div>
<div class="service" style="left:860px"><div class="circle" role="img" aria-label="Photo of two small dogs on leashes beside a car"></div><h3>PET TAXI</h3><p>Grooming, vet drop off/pic up $10.00 each trip Vet appointment visit $30/hr Sed ut perspiciatis unde omnis iste natus</p><span class="btn-outline">READ MORE</span></div>

<h2 class="sec-title" style="top:1012px">WELCOME TO BRINDLE COVE PAW HOUSE</h2>
<svg class="orn" style="top:1064px" viewBox="0 0 240 30"><line x1="0" y1="15" x2="98" y2="15" stroke="#ccc"/><line x1="142" y1="15" x2="240" y2="15" stroke="#ccc"/><circle cx="120" cy="15" r="13" fill="none" stroke="#ccc"/><circle cx="120" cy="15" r="7" fill="var(--orange)"/></svg>
<p class="welcome-text">Hi my name is Marla Ostrand and I would love to introduce myself. I am a Licensed Veterinarian Technician from Nashville, Tennessee. My family and I moved to San Antonio in 2008. I have dedicated the last 13 years to raising my 2 beautiful children and 5 of my furry babies. I have the knowledge and the training to give the special care your pet will need. I was a Licensed Veterinarian Technician Supervisor of a major animal hospital in Nashville. I have spent 20 years of my life taking care of our friends and would do the same for yours.</p>

<section class="testimonials" role="img" aria-label="Dark backdrop photo of a wooded garden">
  <h2 class="sec-title" style="top:50px;color:#fff">TESTIMONIALS</h2>
  <svg class="orn" style="top:100px" viewBox="0 0 240 30"><line x1="0" y1="15" x2="98" y2="15" stroke="rgba(255,255,255,.4)"/><line x1="142" y1="15" x2="240" y2="15" stroke="rgba(255,255,255,.4)"/><circle cx="120" cy="15" r="13" fill="none" stroke="rgba(255,255,255,.5)"/><circle cx="120" cy="15" r="7" fill="var(--orange)"/></svg>
  <div class="quote" style="left:100px"><b>“</b>Sed ut perspiciatis unde omnis iste natus error sit voluptatem accusantium doloremque laudantium, totam rem aperiam, eaque ipsa quae ab illo inventore veritatis et quasi architecto beatae vitae dicta sunt explicabo. Nemo enim ipsam voluptatem</div>
  <div class="quote" style="left:443px"><b>“</b>Sed ut perspiciatis unde omnis iste natus error sit voluptatem accusantium doloremque laudantium, totam rem aperiam, eaque ipsa quae ab illo inventore veritatis et quasi architecto beatae vitae dicta sunt explicabo. Nemo enim ipsam voluptatem</div>
  <div class="quote" style="left:786px"><b>“</b>Sed ut perspiciatis unde omnis iste natus error sit voluptatem accusantium doloremque laudantium, totam rem aperiam, eaque ipsa quae ab illo inventore veritatis et quasi architecto beatae vitae dicta sunt explicabo. Nemo enim ipsam voluptatem</div>
  <div class="author" style="left:118px"><div class="avatar" role="img" aria-label="Client portrait"></div><div><div class="name">Dana Whitlock</div><div class="org">Brindle Cove Paw House</div></div></div>
  <div class="author" style="left:462px"><div class="avatar" role="img" aria-label="Client portrait"></div><div><div class="name">Dana Whitlock</div><div class="org">Brindle Cove Paw House</div></div></div>
  <div class="author" style="left:806px"><div class="avatar" role="img" aria-label="Client portrait"></div><div><div class="name">Dana Whitlock</div><div class="org">Brindle Cove Paw House</div></div></div>
</section>

<h2 class="sec-title" style="top:1740px">PHOTO GALLERY</h2>
<svg class="orn" style="top:1790px" viewBox="0 0 240 30"><line x1="0" y1="15" x2="98" y2="15" stroke="#ccc"/><line x1="142" y1="15" x2="240" y2="15" stroke="#ccc"/><circle cx="120" cy="15" r="13" fill="none" stroke="#ccc"/><circle cx="120" cy="15" r="7" fill="var(--orange)"/></svg>
<div class="gal" style="left:100px;background:linear-gradient(170deg,#6f9a4e,#3c5a2c)" role="img" aria-label="Photo of a white cat standing on a garden chair"></div>
<div class="gal" style="left:355px;background:linear-gradient(170deg,#7a8f5a,#8a6b48)" role="img" aria-label="Photo of a sable collie on a lawn"></div>
<div class="gal" style="left:609px;background:linear-gradient(170deg,#5b5a3c,#4b7a34)" role="img" aria-label="Photo of a tortoise eating greens"></div>
<div class="gal" style="left:860px;background:linear-gradient(170deg,#5f8c3e,#9a9a88)" role="img" aria-label="Photo of a small spaniel on a garden path"></div>

<section class="updates" role="img" aria-label="Backdrop photo of a girl playing in a leafy yard">
  <div class="upd-icon"><span></span></div>
  <h2 class="upd-title">GET NOTIFIED OF ANY UPDATES!</h2>
  <p class="upd-sub">Subscribe below for the beta release and updates</p>
  <div class="subscribe"><div class="field">Enter your E - mail</div><div class="go">SUBSCRIBE</div></div>
</section>

<section class="news">
  <h2 class="news-title"><span></span>CLUB NEWS</h2>
  <div class="news-nav">‹›</div>
  <div class="news-img" style="left:100px;background:linear-gradient(160deg,#8a7a66,#3a332c)" role="img" aria-label="Photo of a black cat indoors"></div>
  <div class="news-body" style="left:310px"><h4>Tucker Boy we will all miss your loving face. With much love.</h4><div class="date">AUG 19, 2016</div><p>Nulla at diam ornare, aliquam urna vel, commodo urna. Nam id risus a est luctus consectetur quis eget libero. Suspendisse potenti. Pellentesque</p><div class="more">Read More +</div></div>
  <div class="news-img" style="left:628px;background:linear-gradient(160deg,#9a6a48,#3a2a22)" role="img" aria-label="Photo of two spaniel dogs together"></div>
  <div class="news-body" style="left:866px"><h4>Tucker Boy we will all miss your loving face. With much love.</h4><div class="date">AUG 19, 2016</div><p>Nulla at diam ornare, aliquam urna vel, commodo urna. Nam id risus a est luctus consectetur quis eget libero. Suspendisse potenti. Pellentesque</p><div class="more">Read More +</div></div>
</section>

<footer class="footer">
  <div class="foot-brand"><span></span>Brindle Cove<br>Paw House</div>
  <div class="foot-col" style="left:330px"><h5>CONTACT US</h5>
    <div class="c-row"><svg width="14" height="18" viewBox="0 0 14 18"><path d="M7 1a6 6 0 0 0-6 6c0 4.5 6 10 6 10s6-5.5 6-10a6 6 0 0 0-6-6z" fill="none" stroke="#fff" stroke-width="1.4"/><circle cx="7" cy="7" r="2" fill="#fff"/></svg><div>Brindle Cove Paw House<br>412 Larkspur Lane, Suite 210</div></div>
    <div class="c-row"><svg width="14" height="14" viewBox="0 0 24 24"><path fill="#fff" d="M6.6 10.8a15 15 0 0 0 6.6 6.6l2.2-2.2c.3-.3.7-.4 1-.2 1.1.4 2.3.6 3.6.6.6 0 1 .4 1 1V20c0 .6-.4 1-1 1A17 17 0 0 1 3 4c0-.6.4-1 1-1h3.5c.6 0 1 .4 1 1 0 1.3.2 2.5.6 3.6.1.3 0 .7-.2 1z"/></svg><div>Phone : +907-555-0199</div></div>
    <div class="c-row"><svg width="16" height="12" viewBox="0 0 16 12"><rect x="0.7" y="0.7" width="14.6" height="10.6" fill="none" stroke="#fff" stroke-width="1.4"/><path d="M1 1l7 6 7-6" fill="none" stroke="#fff" stroke-width="1.4"/></svg><div>info@brindlecovepawhouse.com</div></div>
  </div>
  <div class="foot-col" style="left:654px"><h5>QUICK LINKS</h5>
    <ul class="links"><li>Photo Gallery</li><li>About Us</li><li>Services</li><li>Policies</li><li>Monthly Newsletter</li><li>Payment Methods</li></ul>
  </div>
  <div class="foot-col" style="left:864px;width:250px"><h5>LATEST TWEET`S</h5>
    <div class="tweet"><span class="tb"></span><div><b>@Brindle Cove Paw House</b> Fresh walk slots open this week.<small>1 day ago</small></div></div>
    <div class="tweet"><span class="tb"></span><div><b>@Brindle Cove Paw House</b> Thanks to all our happy pups.<small>1 day ago</small></div></div>
  </div>
</footer>
<div class="copy">Copyright © Brindle Cove Paw House 2016. All rights reserved.</div>

</body>
</html>
```